Lantern Petro - needs a business card

Lantern Petro is a U.S. based diesel sourcing and distribution company that supports American oil & gas fields through providing quality product and consistent services.

Target Market(s)

Oil and Gas

Contact Information for Business Card

The background of the card must be white to ensure the logo pops.

Font styles to use
Serif
Sans Serif

Colors

Designer to choose colors to be used in the design.

Requirements
Must have
• Front of Card: Tag line: Lantern Petro, Powering the Nation's Oil & Gas fields.
• Not sure if you guys do this part but just in case...
• Dale Winterholt
• Owner/CEO
• C:701.555.0148
• E:Dwinterholt@lanternpetro.com
• W:Lanternpetro.com
• Locations: Servicing the Powder River, DJ basin and Bakken formations.
• Back of Card: " Frac fueling is what we do. We understand how important diesel fuel is to your operation, which is why our main service line is Frac fueling. We assure our supply and stand by our service"

```html
<!DOCTYPE html>
<html lang="en">
<head>
<meta charset="utf-8">
<title>Lantern Petro – Business Card</title>
<link href="https://fonts.googleapis.com/css2?family=Open+Sans:wght@400;600;700;800&family=Michroma&display=swap" rel="stylesheet">
<style>
  :root {
    --stage: #2c2c2e;
    --card-white: #ffffff;
    --navy: #0f2d64;
    --red: #c4161c;
    --back-red: #b00d0e;
    --ink: #2a2a2a;
  }
  * { margin: 0; padding: 0; box-sizing: border-box; }
  html, body {
    width: 1200px; height: 1052px; overflow: hidden;
    background: var(--stage);
    font-family: "Open Sans", Arial, sans-serif;
  }
  .stage { position: relative; width: 1200px; height: 1052px; }

  .card {
    position: absolute; left: 220px;
    width: 760px; height: 434px;
    overflow: hidden;
    box-shadow: 0 14px 30px rgba(0,0,0,.45);
  }

  /* Back of card */
  .card--back { top: 70px; background: var(--back-red); color: #fff; text-align: center; }
  .card--back .brand {
    position: absolute; top: 120px; left: 0; right: 0;
    display: flex; justify-content: center; align-items: center; gap: 14px;
  }
  .brand__dot { width: 22px; height: 22px; border-radius: 50%; }
  .card--back .brand__dot { background: #fff; }
  .card--back .brand__name { font-size: 44px; font-weight: 800; color: #fff; letter-spacing: 1px; }
  .back-copy { position: absolute; top: 250px; left: 60px; right: 60px; }
  .back-copy__headline { font-size: 17px; font-weight: 700; margin-bottom: 8px; }
  .back-copy__body { font-size: 16px; line-height: 1.45; }

  /* Front of card */
  .card--front { top: 560px; background: var(--card-white); }
  .card--front .brand {
    position: absolute; top: 42px; left: 40px;
    display: flex; align-items: center; gap: 12px;
  }
  .card--front .brand__dot { background: var(--red); }
  .card--front .brand__name { font-size: 34px; font-weight: 800; color: var(--navy); }

  .locations {
    position: absolute; top: 112px; left: 40px;
    font-size: 16px; line-height: 1.35; color: var(--ink); width: 300px;
  }
  .contact-list { position: absolute; top: 168px; left: 40px; list-style: none; }
  .contact-list li {
    display: flex; align-items: center; gap: 10px;
    font-size: 16px; color: var(--ink); line-height: 27px;
  }
  .contact-list svg { width: 16px; height: 16px; flex: none; }

  .person { position: absolute; top: 178px; right: 44px; text-align: right; }
  .person__name { font-family: "Michroma", Arial, sans-serif; font-size: 22px; font-weight: 400; color: var(--navy); letter-spacing: 1px; -webkit-text-stroke: .8px var(--navy); }
  .person__role { font-family: "Michroma", Arial, sans-serif; font-size: 16px; color: var(--red); margin-top: 4px; }

  .band { position: absolute; left: 0; top: 0; width: 760px; height: 434px; }
  .band-tagline {
    position: absolute; left: 26px; top: 322px;
    font-size: 16px; color: #fff;
    transform: rotate(4.3deg); transform-origin: left top;
  }
</style>
</head>
<body>
<main class="stage">

  <section class="card card--back" aria-label="Back of card">
    <div class="brand">
      <span class="brand__dot"></span>
      <span class="brand__name">Lantern Petro</span>
    </div>
    <div class="back-copy">
      <p class="back-copy__headline">Frac Fueling Is What We Do.</p>
      <p class="back-copy__body">We understand how important diesel fuel is to your operation which is why our main service line is Frac fueling. We assure our supply and stand by our service</p>
    </div>
  </section>

  <section class="card card--front" aria-label="Front of card">
    <svg class="band" viewBox="0 0 760 434" aria-hidden="true">
      <path d="M0 292 L470 327 Q548 332 585 380 Q628 428 690 412 L760 398 L760 434 L0 434 Z" fill="var(--navy)"/>
    </svg>

    <div class="brand">
      <span class="brand__dot"></span>
      <span class="brand__name">Lantern Petro</span>
    </div>

    <p class="locations">Servicing the Powder River DJ basin and Bakken formations.</p>

    <ul class="contact-list">
      <li>
        <svg viewBox="0 0 16 16"><circle cx="8" cy="8" r="8" fill="var(--red)"/><path d="M5.2 4.2l1.6 0 .6 2-1 .8a6 6 0 0 0 2.6 2.6l.8-1 2 .6v1.6c0 .5-.5.9-1 .8A7.2 7.2 0 0 1 4.4 5.2c-.1-.5.3-1 .8-1z" fill="#fff"/></svg>
        701.555.0148
      </li>
      <li>
        <svg viewBox="0 0 16 16"><circle cx="8" cy="8" r="8" fill="var(--red)"/><rect x="4" y="5" width="8" height="6" rx="1" fill="#fff"/><path d="M4.3 5.4 8 8.3l3.7-2.9" stroke="var(--red)" stroke-width="1" fill="none"/></svg>
        dwinterholt@lanternpetro.com
      </li>
      <li>
        <svg viewBox="0 0 16 16"><circle cx="8" cy="8" r="8" fill="var(--red)"/><circle cx="8" cy="8" r="4.2" fill="none" stroke="#fff" stroke-width="1"/><ellipse cx="8" cy="8" rx="1.8" ry="4.2" fill="none" stroke="#fff" stroke-width="1"/><path d="M3.8 8h8.4" stroke="#fff" stroke-width="1"/></svg>
        www.lanternpetro.com
      </li>
    </ul>

    <div class="person">
      <h1 class="person__name">DALE WINTERHOLT</h1>
      <p class="person__role">OWNER/CEO</p>
    </div>

    <p class="band-tagline">Servicing the Powder River, DJ basin and Bakken formations.</p>
  </section>

</main>
</body>
</html>
```